Front Cover Page and Back Cover for Biography Book

Create a book front cover page and back cover for the biography book called Beyond the Tide: The Long Road of Pham Quoc Lanh
Blurb/Summary:
Step into the extraordinary life of Pham Quoc Lanh in Beyond the Tide: The Long Road of Pham Quoc Lanh, a gripping memoir of resilience, determination, and triumph. Born in Quang Ngai, Vietnam, in 1938, Lanh grew up amid the unrelenting challenges of famine, war, and poverty. Yet, his unshakable thirst for education and self-improvement became the foundation of a journey that would defy every expectation.
From studying under flickering oil lamps in hidden village schools during the resistance against French colonial rule to enduring the hardships of the Vietnam War, Lanh’s story is set against the dramatic backdrop of a nation in turmoil. Despite familial and societal obstacles, his passion for knowledge drove him to excel academically and chart a future far beyond the limitations of his humble beginnings.
As a Navy officer, Lanh balanced the rigours of military life with an entrepreneurial spirit that saw him transform his circumstances. Whether selling ice cream, expanding a fleet of fishing boats, or salvaging a sunken ship to create a thriving business, his ingenuity and drive turned adversity into opportunity. Along the way, he navigated personal sacrifices, betrayal, and daring escapes as Vietnam descended into chaos, all while keeping his family at the heart of his efforts.
Through the lens of Lanh’s incredible life, Beyond the Tide highlights the power of education, perseverance, and community in overcoming the impossible. This memoir is not just a story of survival but a testament to human strength, offering readers an inspiring tale of hope, legacy, and the relentless pursuit of a better life. Perfect for those seeking an uplifting narrative with historical and emotional depth, this is a book that will stay with you long after the final page.
Please find the full book attached.
Photos of lanh can be found here in the photo album: https://albums.pictoria-share.example/Xk7RmqTz2wLpYc9Vn

```html
<!DOCTYPE html>
<html lang="en">
<head>
<meta charset="utf-8">
<title>Beyond the Tide – Book Cover Concept</title>
<link rel="stylesheet" href="https://fonts.googleapis.com/css2?family=Barlow:wght@500&family=Inter:wght@500;700;900&family=Allura&display=swap">
<style>
  :root {
    --paper: #ffffff;
    --ink: #111111;
    --white: #ffffff;
    --sky: #93b7dc;
    --scrub: #7a7a52;
    --wood: #9a7a56;
    --spine-top: #9fc2e6;
    --spine-bottom: #c8dcef;
    --portrait: #3c3c42;
    --signature: #f2b43a;
  }
  * { box-sizing: border-box; margin: 0; padding: 0; }
  html, body { width: 1200px; height: 848px; overflow: hidden; background: var(--paper); }
  .sheet { position: relative; width: 1200px; height: 848px; font-family: "Inter", sans-serif; }

  .sheet-title {
    position: absolute; left: 105px; top: 48px;
    font-family: "Barlow", sans-serif; font-weight: 500; font-size: 16px; line-height: 19px; color: var(--ink);
  }
  .sheet-label {
    position: absolute; right: 105px; top: 66px;
    font-family: "Barlow", sans-serif; font-weight: 500; font-size: 16px; color: var(--ink); letter-spacing: 0.2px;
  }

  .spread { position: absolute; left: 105px; top: 124px; width: 990px; height: 600px; display: flex; overflow: hidden; }

  .back-cover, .front-cover { position: relative; height: 100%; overflow: hidden; }
  .back-cover { width: 467px; }
  .front-cover { width: 466px; }

  .cover-photo {
    position: absolute; inset: 0;
    background: linear-gradient(180deg, var(--sky) 0%, var(--scrub) 45%, var(--wood) 100%);
  }

  .blurb {
    position: absolute; left: 46px; top: 144px;
    color: var(--white); font-weight: 500; font-size: 13.2px; line-height: 17.1px; letter-spacing: -0.35px;
  }
  .blurb span { display: block; white-space: nowrap; }
  .blurb p + p { margin-top: 17.1px; }

  .spine {
    position: relative; width: 57px; height: 100%; overflow: hidden;
    background: linear-gradient(180deg, var(--spine-top), var(--spine-bottom));
  }
  .spine-title, .spine-subtitle, .spine-author {
    position: absolute; left: 50%; white-space: nowrap; color: var(--white);
    transform-origin: left top; transform: rotate(90deg);
  }
  .spine-title { top: 30px; margin-left: 23px; font-weight: 900; font-size: 17px; }
  .spine-subtitle { top: 228px; margin-left: 10px; font-weight: 500; font-size: 10px; }
  .spine-portrait {
    position: absolute; left: 0; top: 340px; width: 57px; height: 46px;
    background: linear-gradient(180deg, #9aa2a8, #c9c4bd);
  }
  .spine-author { top: 398px; margin-left: 16px; font-family: "Allura", cursive; font-size: 26px; line-height: 1; }

  .portrait-area {
    position: absolute; left: 251px; top: 58px; width: 215px; height: 542px;
    background: linear-gradient(180deg, #6a6c72, var(--portrait));
  }
  .publisher { position: absolute; left: 32px; top: 54px; font-weight: 700; font-size: 14px; color: var(--ink); }
  .cover-title {
    position: absolute; left: 42px; top: 270px;
    font-weight: 900; font-size: 49px; line-height: 46px; letter-spacing: -1.2px; color: var(--white);
  }
  .cover-subtitle { position: absolute; left: 130px; top: 370px; font-weight: 500; font-size: 14px; color: var(--white); }
  .cover-author {
    position: absolute; left: 222px; top: 386px;
    font-family: "Allura", cursive; font-size: 25px; line-height: 1; color: var(--signature); white-space: nowrap;
  }
</style>
</head>
<body>
<main class="sheet">
  <h1 class="sheet-title">Beyond the Tide:<br>The Long Road of Pham Quoc Lanh</h1>
  <p class="sheet-label">BOOK COVER CONCEPT</p>

  <section class="spread">
    <article class="back-cover">
      <div class="cover-photo" role="img" aria-label="Photo of a wooden boardwalk overlooking coastal scrub and sand dunes under a blue sky"></div>
      <div class="blurb">
        <p>
          <span>Born in 1938, the rugged heart of Quang Ngai province,</span>
          <span>nestled in the central region of Vietnam.</span>
          <span>The land was as unforgiving as it was beautiful—rolling</span>
          <span>hills scarred by years of conflict, rivers winding through</span>
          <span>rice paddies that seemed endless, and the distant</span>
          <span>mountains cloaked in mist.</span>
        </p>
        <p>
          <span>The monsoon rains would come and wash away the</span>
          <span>fragile dirt paths, leaving the villagers stranded, while</span>
          <span>the scorching sun of the dry season cracked the earth</span>
          <span>beneath our feet. It was a land of resilience, where life</span>
          <span>clung to the soil despite the harshness of the times.</span>
        </p>
        <p>
          <span>My family, like many others, was bound to this earth,</span>
          <span>struggling against poverty with every breath.</span>
        </p>
      </div>
    </article>

    <aside class="spine">
      <span class="spine-title">Beyond the Tide</span>
      <span class="spine-subtitle">The Long Road of</span>
      <div class="spine-portrait" role="img" aria-label="Small portrait photo of the author"></div>
      <span class="spine-author">Pham Quoc Lanh</span>
    </aside>

    <article class="front-cover">
      <div class="cover-photo" role="img" aria-label="Photo of a boardwalk railing above coastal dunes and scrubland under a blue sky"></div>
      <div class="portrait-area" role="img" aria-label="Photo of the author, an older man in a dark vest and checked shirt, leaning on the railing"></div>
      <p class="publisher">Publishing Company</p>
      <h2 class="cover-title">Beyond<br>the Tide</h2>
      <p class="cover-subtitle">The Long Road of</p>
      <p class="cover-author">Pham Quoc Lanh</p>
    </article>
  </section>
</main>
</body>
</html>
```